buisnes card for Tranquil Footpath

I need a new business card with my information
Brunhilde Ostrova
BKTPA,LMVD,RN(Grermany)
Cranio-Sacral Reflexology
Facial Reflexology, Halvorkmethode TM
Nerve point Reflexology
41672 Meadowcroft Lane
Abbotsford,BC
Tranquilfootpath.ca
I would like the design to show that I work mostly with clients that have health problems.(80% are back/spine related problems).
I would like the card to be professional as well as inviting. I like nature aspects as well.
I have two websites that I like so you have an Idea what kind of design speaks to me.
1. www.harmonelle.ca the craft of mending (Chilliwack)
2.www.gentlearrivalcare.ca (Abbotsford)

My treatment room is blue and the outside of our house is dark blue and grey. That are colors that could be incorporated

Target Market(s)

clients that are looking for a more natural approach to their health issues

Industry/Entity Type

Health And Wellness

Contact Information for Business Card

Brunhilde Ostrova
BKTPA,LMVD,RN(Grermany)
Cranio-Sacral Reflexology
Nerve point Reflexology
41672 Meadowcroft Lane
Abbotsford,BC
Tranquilfootpath.ca

Colors
0355a3
0492cd

Requirements
Must have
• name, address, phonenumber
Nice to have
• 1. www.harmonelle.ca the craft of mending (Chilliwack)
• 2.www.gentlearrivalcare.ca (Abbotsford)
• This are designs that I like.

```html
<!DOCTYPE html>
<html lang="en">
<head>
<meta charset="utf-8">
<title>Tranquil Footpath – Business Card</title>
<link rel="stylesheet" href="https://fonts.googleapis.com/css2?family=Arimo:wght@400;700&display=swap">
<style>
  :root {
    --backdrop: #1c1c1c;
    --card-blue: #0a93cd;
    --figure-deep: #1b3aa8;
    --figure-mid: #2f5fd0;
    --figure-glow: #c05ac0;
    --text-white: #ffffff;
  }
  html, body {
    margin: 0;
    padding: 0;
    width: 1200px;
    height: 902px;
    overflow: hidden;
    background: var(--backdrop);
  }
  .business-card {
    position: absolute;
    left: 99px;
    top: 164px;
    width: 903px;
    height: 515px;
    overflow: hidden;
    background: var(--card-blue);
    font-family: "Arimo", Helvetica, Arial, sans-serif;
    color: var(--text-white);
  }
  .spine-figure {
    position: absolute;
    left: 60px;
    top: 40px;
    width: 348px;
    height: 437px;
  }
  .contact-block {
    position: absolute;
    left: 448px;
    top: 0;
    right: 0;
    bottom: 0;
  }
  .contact-block > * {
    position: absolute;
    left: 0;
    margin: 0;
    white-space: nowrap;
  }
  .practitioner-name {
    top: 62px;
    font-size: 35px;
    font-weight: 700;
    line-height: 1.2;
  }
  .credentials {
    top: 105px;
    font-size: 21px;
    font-weight: 400;
    line-height: 1.2;
  }
  .services {
    top: 191px;
    padding: 0;
    list-style: none;
    font-size: 23px;
    line-height: 30px;
    font-weight: 400;
  }
  .address {
    top: 319px;
    font-style: normal;
    font-size: 27px;
    line-height: 35px;
    font-weight: 400;
  }
  .website {
    top: 413px;
    font-size: 26px;
    font-weight: 700;
    line-height: 1.2;
  }
</style>
</head>
<body>
  <div class="business-card">
    <svg class="spine-figure" viewBox="0 0 348 437" role="img" aria-label="Illustration of a translucent blue human figure bent forward, spine and skeleton visible, with glowing pain points at the hip, knee and ankle">
      <defs>
        <radialGradient id="bodyTone" cx="50%" cy="50%" r="50%">
          <stop offset="0%" stop-color="var(--figure-mid)" stop-opacity="0.85"/>
          <stop offset="70%" stop-color="var(--figure-deep)" stop-opacity="0.45"/>
          <stop offset="100%" stop-color="var(--figure-deep)" stop-opacity="0"/>
        </radialGradient>
        <radialGradient id="painGlow" cx="50%" cy="50%" r="50%">
          <stop offset="0%" stop-color="var(--figure-glow)" stop-opacity="0.7"/>
          <stop offset="100%" stop-color="var(--figure-glow)" stop-opacity="0"/>
        </radialGradient>
      </defs>
      <ellipse cx="174" cy="218" rx="174" ry="218" fill="url(#bodyTone)"/>
      <ellipse cx="200" cy="260" rx="110" ry="150" fill="url(#painGlow)"/>
    </svg>

    <div class="contact-block">
      <h1 class="practitioner-name">Brunhilde Ostrova</h1>
      <p class="credentials">BKTPA,LMVD,RN(Grermany)</p>
      <ul class="services">
        <li>Cranio-Sacral Reflexology</li>
        <li>Facial Reflexology, Halvorkmethode TM</li>
        <li>Nerve point Reflexology</li>
      </ul>
      <address class="address">41672 Meadowcroft Lane<br>Abbotsford,BC</address>
      <p class="website">Tranquilfootpath.ca</p>
    </div>
  </div>
</body>
</html>
```